Meridian Rest Supply Needs Business Card

Looking for a very nice looking business card. Creative but not extravagant. We sell beds and pillows across the U.S. and need something professional but catchy. I have attached the logo.

Name : Dale Fenwick
Title : President
Phone : (800) 417-2964
Email: sleep@quorvana.com
Website: www.quorvana.com

Can be single-sided or double-sided
horizontal or vertical

Can use Blues/Greys

Target Market(s)

Mass Market

Industry/Entity Type

Retail

Contact Information for Business Card

Name : Dale Fenwick
Title : President
Phone : (800) 417-2964
Email: sleep@quorvana.com
Website: www.quorvana.com

Requirements
Must have
• Clean, Modern, Smooth
• Can use Blues/Greys
• On the other side without the information - have something simple like www.quorvana.com or our logo
Nice to have
• Surprise me
Should not have
• Nothing crazy, nothing cluttered

```html
<!DOCTYPE html>
<html lang="en">
<head>
<meta charset="utf-8">
<title>Meridian Rest Supply – Business Card</title>
<link href="https://fonts.googleapis.com/css2?family=Lato:wght@300;400;700&display=swap" rel="stylesheet">
<style>
  :root {
    --backdrop: #3c3c3c;
    --card-dark: #4b4b4c;
    --card-light: #eef1f4;
    --brand-blue: #3fa6d6;
    --text-white: #ffffff;
    --rule-blue: #5aaedb;
    --muted-white: #e4e7ea;
  }
  * { box-sizing: border-box; margin: 0; padding: 0; }
  html, body {
    width: 1200px; height: 810px; overflow: hidden;
    background: var(--backdrop);
    font-family: "Lato", sans-serif;
  }
  .canvas { position: relative; width: 1200px; height: 810px; }

  .card {
    position: absolute;
    width: 560px; height: 320px;
    border-radius: 22px;
    overflow: hidden;
    box-shadow: 0 6px 18px rgba(0,0,0,0.35);
  }

  /* Logo side */
  .card--logo {
    left: 70px; top: 80px;
    background: var(--card-dark);
    display: flex; flex-direction: column; align-items: center; justify-content: center;
  }
  .wordmark {
    font-family: "Lato", sans-serif;
    font-weight: 300;
    color: var(--brand-blue);
    letter-spacing: 2px;
    line-height: 1;
  }
  .card--logo .wordmark { font-size: 92px; margin-top: -10px; }
  .web-line {
    display: flex; align-items: center; gap: 10px;
    margin-top: 34px;
    font-size: 14px; color: var(--text-white); letter-spacing: 0.3px;
  }
  .web-line .rule { width: 90px; height: 1px; background: var(--rule-blue); }
  .web-line .accent { color: var(--brand-blue); }

  /* Contact side */
  .card--contact {
    left: 570px; top: 450px;
    display: flex;
  }
  .logo-panel {
    width: 290px; height: 100%;
    background: var(--card-light);
    display: flex; align-items: center; justify-content: center;
  }
  .logo-panel .wordmark { font-size: 58px; }
  .info-panel {
    flex: 1; height: 100%;
    background: var(--brand-blue);
    padding: 64px 0 0 30px;
    color: var(--text-white);
  }
  .person-name { font-size: 21px; font-weight: 700; line-height: 1.1; }
  .person-title { font-size: 15px; font-weight: 400; margin: 3px 0 14px 6px; color: var(--muted-white); }
  .contact-list { list-style: none; margin-left: 12px; }
  .contact-list li {
    display: flex; align-items: center; gap: 8px;
    font-size: 15px; line-height: 22px;
  }
  .contact-list svg { width: 13px; height: 13px; fill: var(--text-white); flex: none; }
</style>
</head>
<body>
<div class="canvas">

  <section class="card card--logo" aria-label="Card back with brand name">
    <div class="wordmark">quorvana</div>
    <div class="web-line">
      <span class="rule"></span>
      <span>www.<span class="accent">quorvana</span>.com</span>
      <span class="rule"></span>
    </div>
  </section>

  <section class="card card--contact" aria-label="Card front with contact details">
    <div class="logo-panel">
      <div class="wordmark">quorvana</div>
    </div>
    <div class="info-panel">
      <div class="person-name">Dale Fenwick</div>
      <div class="person-title">President</div>
      <ul class="contact-list">
        <li>
          <svg viewBox="0 0 24 24" aria-hidden="true"><path d="M6.6 10.8a15.1 15.1 0 0 0 6.6 6.6l2.2-2.2a1 1 0 0 1 1-.25 11.4 11.4 0 0 0 3.6.57 1 1 0 0 1 1 1V20a1 1 0 0 1-1 1A17 17 0 0 1 3 4a1 1 0 0 1 1-1h3.5a1 1 0 0 1 1 1c0 1.25.2 2.45.57 3.6a1 1 0 0 1-.25 1z"/></svg>
          (800) 417-2964
        </li>
        <li>
          <svg viewBox="0 0 24 24" aria-hidden="true"><path d="M2 5h20v14H2z" fill="none"/><path d="M2 5h20v2l-10 6L2 7zM2 9l10 6 10-6v10H2z"/></svg>
          sleep@quorvana.com
        </li>
        <li>
          <svg viewBox="0 0 24 24" aria-hidden="true"><circle cx="12" cy="12" r="10" fill="none" stroke="#fff" stroke-width="2"/><path d="M2 12h20M12 2c3 3 3 17 0 20M12 2c-3 3-3 17 0 20" fill="none" stroke="#fff" stroke-width="1.6"/></svg>
          www.quorvana.com
        </li>
      </ul>
    </div>
  </section>

</div>
</body>
</html>
```